Modern Catering Company needs Letterhead Design

We need a letterhead design that will make effective use of the corporate logo and color scheme, along with careful typography, helps this letterhead design communicate the brand well. We do have a corporate logo, however feel free to enhance the color scheme with gold and purple. We are serving a very upscale clientele so the letterhead has to reflect elegance, professionalism, cleanliness, and modern style. We are branding the company so the letterhead and business cards must fit the brand story. There should be no cartoonish elements in the design and we are looking for sharper lines.

Target Market(s)

Businesses and upscale clientele

Industry/Entity Type

Catering

Contact Information for Business Card

while this design can have any number of quirks and distinctions, it needs to be cohesive with the entire brand story clean, professional but edgy

Requirements
Must have
• must have good and carefully placement of it’s logo and where you place the text or the message. Colors blue, very deep purple, jewel tones not pastels, gold. Blue must be the primary color you may accent with purple or gold. Contact information is as follows: Co-Owners/ Chefs: R. Hollowell & T. Brenn, phone: 414-555-0182 email:Contact@emberoakcatering.example, address: 6172 W Larkmoor Ln, Milwaukee, WI 53299
Should not have
• pastel colors, Do not add the BBQ information to the letterhead or business card it was a mistake by the previous designer.

```html
<!DOCTYPE html>
<html lang="en">
<head>
<meta charset="utf-8">
<title>Ember Oak Catering — Letterhead</title>
<link rel="stylesheet" href="https://fonts.googleapis.com/css2?family=Arimo:wght@400;700&family=Open+Sans:wght@400;600&display=swap">
<style>
  :root {
    --backdrop: #d6d6d6;
    --paper: #ffffff;
    --brand-blue: #4a6fbf;
    --ink: #1a1a1a;
    --ink-soft: #3a3a3a;
    --rule-dark: #2b2b2b;
    --watermark: #eef1f7;
    --signature-ink: #c9cbdc;
  }
  * { box-sizing: border-box; margin: 0; padding: 0; }
  html, body { width: 1200px; height: 900px; overflow: hidden; }
  body { background: var(--backdrop); font-family: "Arimo", Arial, sans-serif; color: var(--ink); }

  .letterhead {
    position: absolute; left: 268px; top: 20px;
    width: 664px; height: 860px;
    background: var(--paper);
    box-shadow: 0 4px 14px rgba(0,0,0,.18);
    overflow: hidden;
  }

  .brand-mark {
    position: absolute; left: 64px; top: 20px;
    width: 20px; height: 20px; border-radius: 50%;
    background: var(--brand-blue);
  }
  .brand {
    position: absolute; left: 40px; top: 46px;
    font-family: "Open Sans", Arial, sans-serif; font-weight: 600;
    color: var(--brand-blue); font-size: 20px; line-height: 1.05;
    letter-spacing: .5px; text-transform: uppercase;
  }

  .bar-short { position: absolute; left: 0; top: 84px; width: 34px; height: 8px; background: var(--brand-blue); }
  .bar-long  { position: absolute; left: 172px; top: 100px; right: 0; height: 8px; background: var(--brand-blue); }

  .contact-row {
    position: absolute; left: 176px; right: 20px; top: 80px;
    display: flex; gap: 14px; align-items: center;
    font-family: "Open Sans", Arial, sans-serif; font-size: 9.5px; color: var(--ink-soft);
  }
  .contact-item { display: flex; align-items: center; gap: 4px; white-space: nowrap; }
  .contact-item svg { width: 10px; height: 10px; fill: var(--brand-blue); }

  .watermark {
    position: absolute; left: 60px; top: 170px; width: 560px; height: 520px;
    background: radial-gradient(ellipse at center, var(--watermark) 0%, rgba(238,241,247,0) 70%);
  }

  .letter { position: absolute; left: 40px; top: 196px; width: 584px; font-size: 13px; line-height: 18px; }
  .recipient { margin-bottom: 16px; }
  .letter p { margin-bottom: 16px; }
  .signature {
    width: 70px; height: 26px; margin: -4px 0 4px;
    background: linear-gradient(90deg, var(--signature-ink), rgba(201,203,220,.25));
    border-radius: 3px;
  }
  .signer { font-weight: 700; }

  .footer-rule-blue { position: absolute; left: 0; right: 0; top: 804px; height: 5px; background: var(--brand-blue); }
  .footer-rule-dark { position: absolute; left: 0; right: 0; top: 810px; height: 3px; background: var(--rule-dark); }
  .address {
    position: absolute; left: 0; right: 0; top: 823px; text-align: center;
    font-family: "Open Sans", Arial, sans-serif; font-size: 9.5px; color: var(--ink-soft);
  }
  .footer-band-blue { position: absolute; left: 0; right: 0; bottom: 10px; height: 6px; background: var(--brand-blue); }
  .footer-band-dark { position: absolute; left: 0; right: 0; bottom: 6px; height: 3px; background: var(--rule-dark); }
</style>
</head>
<body>
  <main class="letterhead">
    <span class="brand-mark"></span>
    <div class="brand">Ember Oak<br>Catering</div>
    <div class="bar-short"></div>

    <div class="contact-row">
      <span class="contact-item">
        <svg viewBox="0 0 24 24"><path d="M6.6 10.8a15 15 0 0 0 6.6 6.6l2.2-2.2c.3-.3.7-.4 1-.2 1.1.4 2.3.6 3.6.6.6 0 1 .4 1 1V20c0 .6-.4 1-1 1A17 17 0 0 1 3 4c0-.6.4-1 1-1h3.5c.6 0 1 .4 1 1 0 1.3.2 2.5.6 3.6.1.3 0 .7-.2 1z"/></svg>
        414-555-0182
      </span>
      <span class="contact-item">
        <svg viewBox="0 0 24 24"><path d="M2 5h20v14H2zm2 2v.5l8 5 8-5V7z"/></svg>
        Contact@emberoakcatering.example
      </span>
      <span class="contact-item">R. Hollowell &amp; T. Brenn&nbsp; Co-Owners/ Chefs</span>
    </div>
    <div class="bar-long"></div>

    <div class="watermark" role="img" aria-label="Faint fork, knife and brand symbol watermark"></div>

    <article class="letter">
      <div class="recipient">Lorem Ipsum<br>Lorem Ipsum Admin</div>
      <p>Lorem Ipsum is simply dummy text of the printing and typesetting industry. Lorem Ipsum has been the industry's standard dummy text ever since the 1500s, when an unknown printer took a galley of type and scrambled it to make a type specimen book. It has survived not only five centuries, but also the leap into electronic typesetting, remaining essentially unchanged.</p>
      <p>Lorem Ipsum is simply dummy text of the printing and typesetting industry. Lorem Ipsum has been the industry's standard dummy text ever since the 1500s, when an unknown printer took a galley of type and scrambled it to make a type specimen book.</p>
      <p>It has survived not only five centuries, but also the leap into electronic typesetting, remaining essentially unchanged. Lorem Ipsum is simply dummy text of the printing and typesetting industry. Lorem Ipsum has been the industry's standard dummy text ever since the 1500s, when an unknown printer took a galley of type and scrambled</p>
      <p>Lorem Ipsum is simply dummy text of the printing and typesetting industry. Lorem Ipsum has been the industry's standard dummy text ever since the 1500s, when an unknown printer took a galley of type and scrambled it to make a type specimen book. It has survived not only five centuries, but also the leap into electronic typesetting, remaining essentially unchanged.</p>
      <p>It was popularised in the 1960s with the release of Tyloset sheets containing Lorem Ipsum passages, and more recently with desktop publishing software like Quillpage Studio including versions of Lorem Ipsum.<br>Lorem Ipsum</p>
      <div class="signature" role="img" aria-label="Handwritten signature"></div>
      <div class="signer">Lorem Ipsum Admin</div>
    </article>

    <div class="footer-rule-blue"></div>
    <div class="footer-rule-dark"></div>
    <div class="address">6172 W Larkmoor Ln, Milwaukee, WI 53299</div>
    <div class="footer-band-blue"></div>
    <div class="footer-band-dark"></div>
  </main>
</body>
</html>
```